Tour operator needs simple coded WordPress site (updated extra payment for coding and guaranteed)

[update 9/7/2015]
If you design a new logo and it gets accepted, even if we use another template with your logo you will get $50
[update 8/7/2015]
Update on questions about dual-language
For dual languages we are happy to set up a second site with the same designs in a second language.
For the design aspect just allow the user to switch between languages with an icon.
For the coding, a replica of the site on a second server will do (to save messing around with multiple language plugins) - we will populate it with Chinese text
[original post]
Simple coded WordPress site for tours
You can choose to design only or design and code ($340 design, $150 bonus for coding)
Open design brief - use your creativity
Will be in 2 languages (English and Chinese) but design needs only to be in one language
Winning design will be chosen only from home page, but the winner must make a second standard template page when chosen at no extra cost.
Must be responsive design
We only need homepage and standard template page design and coding, we will populate the pages
You can use design ideas from our pamphlet if you like - attached
Only a sample logo and colors on website and pamphlet - feel free to change as the current ones seem restrictive
Current website framework only to give an idea of the number of pages and basic menu structure (no need to use existing navigation style or any style at all for that matter, open brief)
http://brightwaterlearningtrips.com.au/
Target Market(s)
Chinese parents of kids 10-14 (the kids will take the tour)
Industry/Entity Type
Tour
Number of Pages Required
2 page
Look and feel
Each slider illustrates characteristics of the customer's brand and the style your logo design should communicate.

```html
<!DOCTYPE html>
<html lang="en">
<head>
<meta charset="utf-8">
<title>Kestrel Bay Youth Journeys</title>
<link href="https://fonts.googleapis.com/css2?family=Open+Sans:wght@300;400;600;700&display=swap" rel="stylesheet">
<style>
:root{
  --blue:#1aa3e8;
  --blue-dark:#0d86c4;
  --ink:#333;
  --muted:#888;
  --footer:#262626;
  --line:#e2e2e2;
  --white:#fff;
}
*{box-sizing:border-box;margin:0;padding:0}
html,body{width:1200px;height:3184px;overflow:hidden}
body{font-family:'Open Sans',Arial,sans-serif;color:var(--ink);background:var(--white);font-size:14px}

/* header */
.site-header{height:60px;background:var(--white);border-bottom:1px solid var(--line);position:relative}
.brand{position:absolute;left:80px;top:8px;display:flex;align-items:center;gap:10px}
.brand-mark{width:36px;height:36px;border-radius:50%;background:var(--blue)}
.brand-name{font-weight:700;font-size:26px;color:var(--blue);line-height:1}
.brand-sub{font-size:11px;color:#555;margin-top:2px}
.lang{position:absolute;right:80px;top:6px;display:flex;gap:4px;align-items:center;font-size:9px;color:var(--muted)}
.lang i{display:block;width:14px;height:9px;background:#c8102e}
.lang i+i{background:#1a3d8f}
.main-nav{position:absolute;right:80px;top:22px;display:flex;gap:6px}
.main-nav a{display:block;padding:6px 14px;font-size:11px;font-weight:600;color:#555;text-decoration:none;text-transform:uppercase}
.main-nav a.active{background:var(--blue);color:var(--white)}

/* hero */
.hero{height:530px;position:relative;background:linear-gradient(100deg,#1b2f7a 0%,#263f96 35%,#3b5fb0 60%,#5a7fbf 80%,#9bb6d8 100%)}
.hero-caption{position:absolute;right:100px;top:200px;width:560px;background:rgba(0,0,0,.75);color:var(--white);padding:18px 20px}
.hero-caption h2{font-weight:400;font-size:24px;margin-bottom:10px}
.hero-caption p{font-size:11px;line-height:1.5;color:#ddd}
.hero-arrow{position:absolute;top:245px;color:var(--white);font-size:28px}
.hero-arrow.prev{left:40px}.hero-arrow.next{right:40px}
.dots{position:absolute;bottom:24px;left:50%;transform:translateX(-50%);display:flex;gap:8px}
.dots span{width:10px;height:10px;border-radius:50%;background:rgba(255,255,255,.5)}
.dots span.on{background:var(--white)}

/* section heading */
.sec-title{display:flex;align-items:center;justify-content:center;gap:30px;color:var(--blue);font-size:40px;font-weight:400}
.sec-title::before,.sec-title::after{content:"";width:300px;height:1px;background:#ccd}
.lead{text-align:center;color:#aaa;font-size:13px;line-height:2;width:960px;margin:0 auto}

/* welcome */
.welcome{height:770px;padding-top:90px}
.welcome .lead{margin-top:36px}
.features{display:flex;justify-content:center;gap:140px;margin-top:60px}
.feature{width:220px;text-align:center}
.feature .icon{width:84px;height:84px;border-radius:50%;background:#444;margin:0 auto;display:flex;align-items:center;justify-content:center}
.feature .icon.blue{background:var(--blue)}
.feature h3{font-size:18px;font-weight:600;margin:26px 0 12px}
.feature p{font-size:11px;color:var(--muted);line-height:1.6}

/* solutions */
.solutions{height:320px;background:linear-gradient(180deg,rgba(30,30,30,.9),rgba(20,20,20,.92)),linear-gradient(90deg,#5a4a3a,#3a3a3a,#6b5a48);color:var(--white);text-align:center;padding-top:42px}
.solutions h2{font-size:34px;font-weight:600}
.solutions p{font-size:13px;line-height:1.8;width:1080px;margin:16px auto 0;color:#ddd}
.pillars{display:flex;justify-content:center;gap:110px;margin-top:22px;font-size:14px;font-weight:600}
.pillars div svg{display:block;margin:0 auto 8px}

/* special tour */
.special{height:660px;padding-top:46px}
.special .lead{margin-top:30px;line-height:1.8}
.tour-box{width:1000px;margin:80px auto 0;height:232px;background:#3a3a3a}
.tour-head{height:60px;background:var(--blue);color:var(--white);display:flex;align-items:center;justify-content:space-between;padding:0 0 0 28px;font-size:26px;font-weight:600}
.tour-head .ctl{display:flex;gap:4px;margin-right:6px}
.tour-head .ctl span{width:30px;height:40px;background:var(--blue-dark);display:flex;align-items:center;justify-content:center;font-size:18px}
.tour-body{display:flex;height:172px;color:var(--white)}
.tour-info{width:300px;padding:22px 28px;border-right:1px solid #555}
.tour-info h4{font-size:14px;margin-bottom:10px}
.tour-info p{font-size:11px;color:#ccc;line-height:1.6}
.tour-gallery{flex:1;padding:22px 20px;position:relative}
.tour-gallery .cap{font-size:12px;margin-bottom:14px}
.thumbs{display:flex;gap:8px;padding-left:24px}
.thumbs div{width:86px;height:64px}
.tour-gallery .arr{position:absolute;top:90px;font-size:20px;color:#aaa}

/* testimonials */
.students{height:300px;background:linear-gradient(180deg,rgba(20,20,20,.82),rgba(20,20,20,.88)),linear-gradient(90deg,#4a5560,#2c3238,#56606a);color:var(--white);text-align:center;padding-top:26px}
.students h2{font-size:30px;font-weight:400}
.quote-row{display:flex;align-items:center;justify-content:center;gap:50px;margin-top:16px}
.avatar{width:90px;height:90px;border-radius:50%;border:4px solid var(--white);background:linear-gradient(135deg,#8aa0b8,#3d5570)}
.quote-row span{font-size:26px}
.student-name{font-weight:600;margin-top:10px;font-size:14px}
.students p{font-size:12px;line-height:1.7;color:#ddd;width:900px;margin:10px auto 0}

/* social */
.social{height:120px;display:flex;justify-content:center;align-items:center;gap:36px}
.social span{width:52px;height:52px;border-radius:50%;background:#555}
.social span.on{background:var(--blue)}

/* footer */
.site-footer{height:424px;background:var(--footer);color:#ccc;position:relative}
.cols{display:flex;padding:60px 0 0 120px}
.col{width:350px}
.col h5{color:var(--white);font-size:13px;font-weight:700;text-transform:uppercase;margin-bottom:20px}
.col li{list-style:none;font-size:12px;margin-bottom:22px;padding-left:16px;position:relative}
.col li::before{content:"›";position:absolute;left:0;color:var(--blue)}
.field{width:230px;height:30px;background:#3a3a3a;border:1px solid #4a4a4a;font-size:11px;color:#999;padding:7px 10px;margin-bottom:12px}
.send{width:90px;height:30px;background:var(--blue);color:var(--white);font-size:12px;font-weight:600;display:flex;align-items:center;justify-content:center;margin-left:140px}
.copy{position:absolute;left:0;right:0;bottom:0;height:44px;border-top:1px solid #3a3a3a;font-size:10px;color:#888;text-align:right;padding:16px 120px 0}
</style>
</head>
<body>

<header class="site-header">
  <div class="brand">
    <span class="brand-mark"></span>
    <div>
      <div class="brand-name">KBJ</div>
      <div class="brand-sub">Kestrel Bay Youth Journeys</div>
    </div>
  </div>
  <div class="lang">Language <i></i><i></i></div>
  <nav class="main-nav">
    <a class="active" href="#">Home</a><a href="#">About us</a><a href="#">Tours</a><a href="#">Contact</a>
  </nav>
</header>

<section class="hero" role="img" aria-label="Slider photo: waving national flag beside a harbour opera house under blue sky">
  <span class="hero-arrow prev">‹</span>
  <span class="hero-arrow next">›</span>
  <div class="hero-caption">
    <h2>Promoting Cultural Exchange</h2>
    <p>14-day premium cultural and educational tours to Australian cities. Educational, safe, culturally enlightening and fun. Learn about educational institutions, history, sports, laws and customs, food and culture.</p>
  </div>
  <div class="dots"><span class="on"></span><span></span><span></span></div>
</section>

<section class="welcome">
  <h2 class="sec-title">Welcome!</h2>
  <p class="lead">At Kestrel Bay Youth Journeys we are passionate about educational travel and providing opportunities for students to learn more about Australia and gain a deeper understanding of the culture. The out of classroom experience gained on our trips is invaluable. Taking the Kestrel Bay journey is easy because our team of dedicated experts assists every step of the way – from meticulously planning the curriculum to providing every detail of your trip to accompanying you on tour.</p>
  <div class="features">
    <div class="feature">
      <div class="icon blue"><svg width="40" height="40" viewBox="0 0 40 40"><path d="M6 10h12c2 0 2 2 2 2v20s0-2-2-2H6zM34 10H22c-2 0-2 2-2 2v20s0-2 2-2h12z" fill="#fff"/></svg></div>
      <h3>Education</h3>
      <p>Lorem ipsum dolor sit amet, consectetur adipisicing elit, sed do eiusmod tempor incididunt ut labore et dolore magna aliqua.</p>
    </div>
    <div class="feature">
      <div class="icon"><svg width="40" height="40" viewBox="0 0 40 40"><circle cx="20" cy="20" r="15" fill="none" stroke="#fff" stroke-width="3"/><path d="M26 14l-4 8-8 4 4-8z" fill="#fff"/></svg></div>
      <h3>Travel</h3>
      <p>Lorem ipsum dolor sit amet, consectetur adipisicing elit, sed do eiusmod tempor incididunt ut labore et dolore magna aliqua.</p>
    </div>
    <div class="feature">
      <div class="icon"><svg width="40" height="40" viewBox="0 0 40 40"><circle cx="20" cy="20" r="15" fill="none" stroke="#fff" stroke-width="3"/><ellipse cx="20" cy="20" rx="6" ry="15" fill="none" stroke="#fff" stroke-width="2"/><path d="M5 20h30" stroke="#fff" stroke-width="2"/></svg></div>
      <h3>Culture</h3>
      <p>Lorem ipsum dolor sit amet, consectetur adipisicing elit, sed do eiusmod tempor incididunt ut labore et dolore magna aliqua.</p>
    </div>
  </div>
</section>

<section class="solutions" role="img" aria-label="Background photo: students working together at a table">
  <h2>We craft practical solutions</h2>
  <p>Lorem ipsum dolor sit amet, consectetur adipisicing elit, sed do eiusmod tempor incididunt ut labore et dolore magna aliqua. Ut enim ad minim veniam Lorem ipsum dolor sit amet, consectetur adipisicing elit, sed do eiusmod tempor incididunt ut labore et dolore magna aliqua. Ut enim ad minim veniam Lorem ipsum dolor sit amet, consectetur adipisicing elit, sed do eiusmod tempor incididunt ut labore et dolore magna aliqua. Ut enim ad minim veniam.</p>
  <div class="pillars">
    <div><svg width="22" height="22" viewBox="0 0 22 22"><circle cx="11" cy="7" r="4" fill="#fff"/><path d="M3 20c0-5 4-7 8-7s8 2 8 7z" fill="#fff"/></svg>Cultural education</div>
    <div><svg width="22" height="22" viewBox="0 0 22 22"><path d="M2 12l18-9-6 17-3-7z" fill="#fff"/></svg>Cultural activities</div>
    <div><svg width="22" height="22" viewBox="0 0 22 22"><circle cx="11" cy="11" r="8" fill="none" stroke="#fff" stroke-width="2"/><path d="M11 5v6l4 3" stroke="#fff" stroke-width="2" fill="none"/></svg>Cultural Tours</div>
  </div>
</section>

<section class="special">
  <h2 class="sec-title">Special Tour</h2>
  <p class="lead">Lorem ipsum dolor sit amet, consectetur adipisicing elit, sed do eiusmod tempor incididunt ut labore et dolore magna aliqua. Ut enim ad minim veniam Lorem ipsum dolor sit amet, consectetur adipisicing elit, sed do eiusmod tempor.</p>
  <div class="tour-box">
    <div class="tour-head">July<div class="ctl"><span>‹</span><span>›</span></div></div>
    <div class="tour-body">
      <div class="tour-info">
        <h4>July 4th - July 17th 2015</h4>
        <p>Lorem ipsum dolor sit amet, consectetur adipisicing elit, sed do eiusmod tempor incididunt.</p>
      </div>
      <div class="tour-gallery">
        <div class="cap">12 places available</div>
        <span class="arr" style="left:14px">‹</span>
        <div class="thumbs">
          <div role="img" aria-label="Tour photo: harbour at sunset" style="background:linear-gradient(#e8a050,#7a4a2a)"></div>
          <div role="img" aria-label="Tour photo: city skyline and water" style="background:linear-gradient(#7ab0d8,#3a6a90)"></div>
          <div role="img" aria-label="Tour photo: beach coastline" style="background:linear-gradient(#9ad0e8,#d8c49a)"></div>
          <div role="img" aria-label="Tour photo: group of students" style="background:linear-gradient(#6a8aa8,#44566a)"></div>
          <div role="img" aria-label="Tour photo: wildlife park" style="background:linear-gradient(#8ab06a,#4a6a3a)"></div>
          <div role="img" aria-label="Tour photo: campus building" style="background:linear-gradient(#b0c4d8,#6a7a8a)"></div>
          <div role="img" aria-label="Tour photo: classroom visit" style="background:linear-gradient(#c8b090,#6a5a48)"></div>
        </div>
        <span class="arr" style="right:14px">›</span>
      </div>
    </div>
  </div>
</section>

<section class="students" role="img" aria-label="Background photo: graduates celebrating outdoors">
  <h2>Words from students</h2>
  <div class="quote-row"><span>‹</span><div class="avatar" role="img" aria-label="Student portrait"></div><span>›</span></div>
  <div class="student-name">Lena Hart</div>
  <p>Lorem ipsum dolor sit amet, consectetur adipisicing elit, sed do eiusmod tempor incididunt ut labore et dolore magna aliqua. Ut enim ad minim veniam Lorem ipsum dolor sit amet, consectetur adipisicing elit, sed do eiusmod tempor incididunt ut labore et dolore.</p>
</section>

<section class="social" aria-label="Social links">
  <span></span><span></span><span></span><span class="on"></span><span></span>
</section>

<footer class="site-footer">
  <div class="cols">
    <div class="col">
      <h5>Navigation links</h5>
      <ul><li>Home</li><li>About us</li><li>Tours</li><li>Contact</li></ul>
    </div>
    <div class="col">
      <h5>Tours</h5>
      <ul><li>Tour dates</li><li>Safety and security</li><li>Terms and conditions</li><li>Travel insurance</li></ul>
    </div>
    <div class="col">
      <h5>Receive our newsletter</h5>
      <div class="field">Name</div>
      <div class="field">Email</div>
      <div class="send">SEND</div>
    </div>
  </div>
  <div class="copy">Copyright © 2015 Kestrel Bay Youth Journeys</div>
</footer>

</body>
</html>
```